Koveli Seafood Shipping Packaging Re-Design

We need a packaging (Shipping Carton) design for our Seafood Products (FROZEN). We already have a basic packaging design which we prefer to have a modern touch on it.
Spec :
1. It must show our logo (Attached), note that the text of "KOVELI" which accompany the logo is optional, it can be omitted & showing only the logo.
2. Main color is Blue
3. Our carton is regular shipping box with dimension L43cm x W 27cm x H 16cm.
4. Our material of Carton is both Brown & White Kraft Paperboard, so the design should look nice in both material.

Attached our Logo and packaging design.

Target Market(s)

Frozen Seafood Distributor & Seafood Buyer

Industry/Entity Type

Food Production

Requirements
Must have
• 1. Must Show our Logo
• 2. Main Color of the Text/Logo is Blue
• 3. On the side of the packaging / Carton must show two box of CODE & SIZE
• 4. Must Show these icons :
• a. Handle with Care
• b. Maximum Stackable 10 Carton
• c. Recyleable Material
• d. Protect from the Water/Rain
Nice to have
• Would prefer to have a modern design

```html
<!DOCTYPE html>
<html lang="en">
<head>
<meta charset="utf-8">
<title>Koveli Shipping Carton</title>
<link href="https://fonts.googleapis.com/css2?family=Cinzel:wght@500&display=swap" rel="stylesheet">
<style>
  :root {
    --canvas: #ffffff;
    --board-white: #f1f1f1;
    --board-kraft: #b3957a;
    --brand-navy: #1b3f8f;
    --line-blue: #2a63b4;
    --wave-pale: #e4f1fb;
    --wave-light: #9fcdee;
    --wave-mid: #4fa6dd;
    --wave-deep: #0b6cb2;
    --fold: rgba(0,0,0,0.12);
  }
  * { box-sizing: border-box; margin: 0; padding: 0; }
  html, body { width: 1200px; height: 909px; overflow: hidden; background: var(--canvas); }
  .canvas { position: relative; width: 1200px; height: 909px; font-family: "Cinzel", serif; }

  .panel { position: absolute; overflow: hidden; }
  .board-white { background: var(--board-white); }
  .board-kraft { background: var(--board-kraft); }

  .wave-band {
    position: absolute; top: 0; bottom: 0;
    background: linear-gradient(90deg, var(--wave-pale) 0%, var(--wave-light) 14%, var(--wave-mid) 30%, var(--wave-deep) 50%, var(--wave-mid) 70%, var(--wave-light) 86%, var(--wave-pale) 100%);
  }
  .wave-band.edge-left { background: linear-gradient(90deg, var(--wave-deep) 0%, var(--wave-mid) 40%, var(--wave-light) 72%, var(--wave-pale) 100%); }
  .wave-band.edge-right { background: linear-gradient(90deg, var(--wave-pale) 0%, var(--wave-light) 30%, var(--wave-mid) 60%, var(--wave-deep) 100%); }

  .fold-line { position: absolute; left: 0; right: 0; height: 1px; background: var(--fold); }

  .address-box { position: absolute; width: 165px; height: 28px; border: 2px solid var(--line-blue); border-radius: 3px; }

  .brand-mini { position: absolute; display: flex; align-items: center; gap: 3px; color: var(--brand-navy); font-size: 9px; font-weight: 500; letter-spacing: 0.5px; }
  .brand-mini.upside { transform: rotate(180deg); }
  .brand-mini .dot { width: 10px; height: 10px; border-radius: 50%; background: var(--brand-navy); }

  .brand-main { position: absolute; display: flex; flex-direction: column; align-items: center; gap: 10px; color: var(--brand-navy); }
  .brand-main .dot { width: 100px; height: 100px; border-radius: 50%; background: var(--brand-navy); }
  .brand-main .name { font-size: 36px; font-weight: 500; letter-spacing: 4px; }

  .info-box { position: absolute; width: 120px; height: 132px; border: 2px solid var(--line-blue); border-radius: 5px; }
  .info-box::after { content: ""; position: absolute; left: 0; right: 0; top: 25px; height: 2px; background: var(--line-blue); }

  .icon-row { position: absolute; display: flex; gap: 6px; }
  .icon-row svg { width: 38px; height: 38px; }
</style>
</head>
<body>
<svg width="0" height="0" style="position:absolute">
  <defs>
    <g id="icon-care"><circle cx="19" cy="19" r="18" fill="none" stroke="#2a63b4" stroke-width="1.4"/><path d="M9 18 q0 9 10 11 q10-2 10-11" fill="none" stroke="#2a63b4" stroke-width="2.2"/><rect x="14" y="11" width="10" height="9" fill="#2a63b4"/></g>
    <g id="icon-stack"><circle cx="19" cy="19" r="18" fill="none" stroke="#2a63b4" stroke-width="1.4"/><text x="19" y="21" text-anchor="middle" font-family="Arial, sans-serif" font-weight="700" font-size="12" fill="#2a63b4">10</text><path d="M11 25 h16 M11 28 h16" stroke="#2a63b4" stroke-width="1.6"/></g>
    <g id="icon-rain"><circle cx="19" cy="19" r="18" fill="none" stroke="#2a63b4" stroke-width="1.4"/><path d="M8 19 q11-13 22 0 z" fill="#2a63b4"/><path d="M19 19 v9 q0 3-3 2" fill="none" stroke="#2a63b4" stroke-width="1.8"/></g>
    <g id="icon-recycle"><circle cx="19" cy="19" r="18" fill="none" stroke="#2a63b4" stroke-width="1.4"/><path d="M19 10 l7 12 h-14 z" fill="none" stroke="#2a63b4" stroke-width="2.6" stroke-linejoin="round"/></g>
    <g id="icon-up"><circle cx="19" cy="19" r="18" fill="none" stroke="#2a63b4" stroke-width="1.4"/><path d="M15 19 v-9 M23 19 v-9 M12 13 l3-3 3 3 M20 13 l3-3 3 3" fill="none" stroke="#2a63b4" stroke-width="1.8"/><text x="19" y="29" text-anchor="middle" font-family="Arial, sans-serif" font-size="9" fill="#2a63b4">up</text></g>
  </defs>
</svg>

<main class="canvas">

  <!-- White board: top flaps + front -->
  <section class="panel board-white" style="left:52px; top:72px; width:632px; height:300px;" aria-label="White carton long side">
    <div class="wave-band" role="img" aria-label="Wavy blue water stripes" style="left:0; width:190px;"></div>
    <div class="wave-band edge-right" role="img" aria-label="Wavy blue water stripes" style="right:0; width:66px;"></div>
    <div class="fold-line" style="top:44px;"></div>
    <div class="fold-line" style="top:88px;"></div>
    <div class="brand-mini" style="left:198px; top:24px;"><span class="dot"></span>KOVELI</div>
    <div class="brand-mini upside" style="left:500px; top:54px;"><span class="dot"></span>KOVELI</div>
    <div class="address-box" style="left:376px; top:8px;"></div>
    <div class="address-box" style="left:192px; top:50px;"></div>
    <div class="brand-main" style="left:270px; top:110px;"><span class="dot"></span><span class="name">KOVELI</span></div>
  </section>

  <!-- White board: end panel -->
  <section class="panel board-white" style="left:712px; top:153px; width:400px; height:214px;" aria-label="White carton short side">
    <div class="wave-band edge-left" role="img" aria-label="Wavy blue water stripes" style="left:0; width:70px;"></div>
    <div class="info-box" style="left:92px; top:17px;"></div>
    <div class="info-box" style="left:218px; top:17px;"></div>
    <div class="icon-row" style="left:106px; top:162px;">
      <svg role="img" aria-label="Handle with care"><use href="#icon-care"/></svg>
      <svg role="img" aria-label="Stack maximum 10"><use href="#icon-stack"/></svg>
      <svg role="img" aria-label="Keep dry"><use href="#icon-rain"/></svg>
      <svg role="img" aria-label="Recyclable"><use href="#icon-recycle"/></svg>
      <svg role="img" aria-label="This way up"><use href="#icon-up"/></svg>
    </div>
  </section>

  <!-- Kraft board: top flaps + front -->
  <section class="panel board-kraft" style="left:64px; top:500px; width:636px; height:298px;" aria-label="Kraft carton long side">
    <div class="wave-band" role="img" aria-label="Wavy blue water stripes" style="left:12px; width:178px;"></div>
    <div class="wave-band edge-right" role="img" aria-label="Wavy blue water stripes" style="right:0; width:80px;"></div>
    <div class="fold-line" style="top:42px;"></div>
    <div class="fold-line" style="top:86px;"></div>
    <div class="brand-mini" style="left:206px; top:22px;"><span class="dot"></span>KOVELI</div>
    <div class="brand-mini upside" style="left:498px; top:52px;"><span class="dot"></span>KOVELI</div>
    <div class="address-box" style="left:380px; top:8px;"></div>
    <div class="address-box" style="left:196px; top:48px;"></div>
    <div class="brand-main" style="left:286px; top:108px;"><span class="dot"></span><span class="name">KOVELI</span></div>
  </section>

  <!-- Kraft board: end panel -->
  <section class="panel board-kraft" style="left:762px; top:560px; width:404px; height:222px;" aria-label="Kraft carton short side">
    <div class="wave-band edge-left" role="img" aria-label="Wavy blue water stripes" style="left:0; width:72px;"></div>
    <div class="info-box" style="left:95px; top:17px;"></div>
    <div class="info-box" style="left:226px; top:17px;"></div>
    <div class="icon-row" style="left:110px; top:170px;">
      <svg role="img" aria-label="Handle with care"><use href="#icon-care"/></svg>
      <svg role="img" aria-label="Stack maximum 10"><use href="#icon-stack"/></svg>
      <svg role="img" aria-label="Keep dry"><use href="#icon-rain"/></svg>
      <svg role="img" aria-label="Recyclable"><use href="#icon-recycle"/></svg>
      <svg role="img" aria-label="This way up"><use href="#icon-up"/></svg>
    </div>
  </section>

</main>
</body>
</html>
```